New Board Game - TRY 45:35:20

The project is in two phases:
A. GAME BOARD DESIGN
Design of a striking game board.
NB. See the following files:
* TRY 45:35:20 Background Info
* TRY 45:35:20 Game Board Format
NB. The contest fee is for Phase A only. Additional fees will be paid for Phase B.
B. APPLICATION OF GAME BOARD DESIGN
The game board design will to be applied to the following game materials:
* Game cards (front and back)
* Sticker for game board tube
* Facilitator's Handbook front and back cover
* Icon for pages inside Facilitator's Handbook
Additional information on the game cards will be provided to the winning designer.
Please note that the project fee is for Phase A only. We will pay additional fees for Phase B, i.e. game cards etc.
NOTE:
Please keep in mind that the game will be used in a corporate setting. The initial target group are Learning and Development (L&D) specialists, mainly people who develop or deliver training courses. They are all educated professionals.
I recently included this feedback in a message to one of the designers:
The game board has to have a level of sophistication and elegance that suits a corporate environment. The game will also be the first direct contact that some potential members will have with the Collegium and has to make a positive impression on them.
We want people to perceive the game as a top-class, creative product.
PLEASE NOTE:
The project fee is now a guaranteed payment.
Target Market(s)
The game will initially be used at networking events held by the Collegium of Skill Advisors in Australia (see: www.csaglobalnet.org). These events are attended by members and guests, with the group ranging from 10 to 20 attendees.
The game may also be used as part of management or leadership development programs in business and government organisations.
Another possible use is with teachers at networking events or professional development courses.
Requirements
Must have
- See the uploaded files for important design requirements.
What is most important is that the game materials are attractive, appealing, impactful. People (in the target group) who see the game materials should feel that they want to find out more, pick up the cards and play the game.
Should not have
- Still thinking....

```html
<!DOCTYPE html>
<html lang="en">
<head>
<meta charset="utf-8">
<title>TRY 45:35:20 – Game Board</title>
<link href="https://fonts.googleapis.com/css2?family=Source+Sans+3:wght@600;700;800&family=Bangers&display=swap" rel="stylesheet">
<style>
  :root{
    --page:#ffffff;
    --navy:#020a6b;
    --lime:#8ccc1c;
    --white:#ffffff;
    --orange-hi:#ff9a1a;
    --orange-lo:#ff4f00;
    --green-hi:#9fdc2a;
    --green-lo:#4ea812;
    --blue-hi:#3fd0ff;
    --blue-lo:#0a78e0;
    --yellow-hi:#ffe14a;
    --yellow-lo:#ffbf00;
    --ink:#1a1a1a;
    --red-hi:#ff3a2a;
    --red-lo:#b30000;
    --burst:#ff6a1a;
  }
  *{margin:0;padding:0;box-sizing:border-box}
  html,body{width:1200px;height:900px;overflow:hidden;background:var(--page)}
  .canvas{position:relative;width:1200px;height:900px;font-family:"Source Sans 3",Arial,sans-serif}
  .board{position:absolute;left:172px;top:44px;width:862px;height:720px;background:var(--navy);border:8px solid var(--lime)}
  .track{position:absolute;left:186px;top:59px;width:834px;height:690px;background:var(--white);border-radius:78px}
  .track-inner{position:absolute;left:276px;top:149px;width:654px;height:510px;background:var(--navy);border-radius:4px}
  .corners{position:absolute;left:0;top:0}
  .corner-word{font-family:"Bangers",Impact,sans-serif;font-size:40px;fill:var(--burst);stroke:var(--red-lo);stroke-width:1.5px;letter-spacing:1px}

  .tile{position:absolute;width:64px;height:76px;border-radius:5px;display:flex;align-items:center;justify-content:center;color:var(--white);font-weight:700;font-size:27px;letter-spacing:-.5px}
  .tile sup{font-size:11px;vertical-align:top;position:relative;top:4px;margin-left:1px}
  .tile--side{width:76px;height:64px}
  .tile--side .tile-face{transform:rotate(90deg)}
  .tile--right .tile-face{transform:rotate(-90deg)}
  .tile--top .tile-face{transform:rotate(180deg)}
  .tile-face{display:flex;align-items:center;justify-content:center}
  .tile--orange{background:linear-gradient(135deg,var(--orange-hi),var(--orange-lo))}
  .tile--green{background:linear-gradient(135deg,var(--green-hi),var(--green-lo))}
  .tile--blue{background:linear-gradient(135deg,var(--blue-hi),var(--blue-lo))}
  .tile--yellow{background:linear-gradient(135deg,var(--yellow-hi),var(--yellow-lo))}
  .badge{width:46px;height:46px;border:2px solid var(--ink);border-radius:50%;display:flex;flex-direction:column;align-items:center;justify-content:center;color:var(--ink);font-size:12px;font-weight:800;line-height:1;text-transform:none}
  .badge span{display:block}

  .title{position:absolute;left:372px;top:250px;width:460px;text-align:center;color:var(--white);font-weight:700;line-height:.9}
  .title-word{display:block;font-size:190px;letter-spacing:-6px}
  .title-ratio{display:block;font-size:84px;letter-spacing:-2px;margin-top:6px}

  .credit{position:absolute;color:var(--white);font-size:6.5px;white-space:nowrap}
  .credit--bottom{left:350px;top:651px}
  .credit--top{left:676px;top:148px;transform:rotate(180deg)}
</style>
</head>
<body>
<div class="canvas">
  <div class="board"></div>
  <div class="track"></div>
  <div class="track-inner"></div>

  <svg class="corners" width="1200" height="900" viewBox="0 0 1200 900" aria-hidden="true">
    <defs>
      <radialGradient id="cornerRed" cx="50%" cy="50%" r="70%">
        <stop offset="0" stop-color="var(--red-hi)"/>
        <stop offset="1" stop-color="var(--red-lo)"/>
      </radialGradient>
    </defs>
    <path fill="url(#cornerRed)" d="M193,222 V140 Q193,66 267,66 H348 V142 H292 Q270,142 270,164 V222 Z"/>
    <path fill="url(#cornerRed)" d="M1013,222 V140 Q1013,66 939,66 H858 V142 H914 Q936,142 936,164 V222 Z"/>
    <path fill="url(#cornerRed)" d="M193,586 V668 Q193,742 267,742 H348 V666 H292 Q270,666 270,644 V586 Z"/>
    <path fill="url(#cornerRed)" d="M1013,586 V668 Q1013,742 939,742 H858 V666 H914 Q936,666 936,644 V586 Z"/>
    <text class="corner-word" text-anchor="middle" transform="translate(244,134) rotate(140)">YIKES!</text>
    <text class="corner-word" text-anchor="middle" transform="translate(962,134) rotate(-140)">OOPS!</text>
    <text class="corner-word" text-anchor="middle" transform="translate(246,690) rotate(40)">UH-OH!</text>
    <text class="corner-word" text-anchor="middle" transform="translate(960,690) rotate(-40)">CRIKEY!</text>
  </svg>

  <!-- top row -->
  <div class="tile tile--top tile--green" style="left:352px;top:66px"><div class="tile-face">35<sup>%</sup></div></div>
  <div class="tile tile--top tile--yellow" style="left:424px;top:66px"><div class="tile-face"><div class="badge"><span>ROLL</span><span>again</span></div></div></div>
  <div class="tile tile--top tile--orange" style="left:496px;top:66px"><div class="tile-face">45<sup>%</sup></div></div>
  <div class="tile tile--top tile--orange" style="left:568px;top:66px"><div class="tile-face">45<sup>%</sup></div></div>
  <div class="tile tile--top tile--orange" style="left:640px;top:66px"><div class="tile-face">45<sup>%</sup></div></div>
  <div class="tile tile--top tile--yellow" style="left:712px;top:66px"><div class="tile-face"><div class="badge"><span>ANY</span><span>card</span></div></div></div>
  <div class="tile tile--top tile--blue" style="left:784px;top:66px"><div class="tile-face">20<sup>%</sup></div></div>

  <!-- bottom row -->
  <div class="tile tile--orange" style="left:352px;top:666px"><div class="tile-face">45<sup>%</sup></div></div>
  <div class="tile tile--yellow" style="left:424px;top:666px"><div class="tile-face"><div class="badge"><span>ANY</span><span>card</span></div></div></div>
  <div class="tile tile--green" style="left:496px;top:666px"><div class="tile-face">35<sup>%</sup></div></div>
  <div class="tile tile--green" style="left:568px;top:666px"><div class="tile-face">35<sup>%</sup></div></div>
  <div class="tile tile--blue" style="left:640px;top:666px"><div class="tile-face">20<sup>%</sup></div></div>
  <div class="tile tile--yellow" style="left:712px;top:666px"><div class="tile-face"><div class="badge"><span>ROLL</span><span>again</span></div></div></div>
  <div class="tile tile--orange" style="left:784px;top:666px"><div class="tile-face">45<sup>%</sup></div></div>

  <!-- left column -->
  <div class="tile tile--side tile--green" style="left:193px;top:230px"><div class="tile-face">35<sup>%</sup></div></div>
  <div class="tile tile--side tile--blue" style="left:193px;top:302px"><div class="tile-face">20<sup>%</sup></div></div>
  <div class="tile tile--side tile--yellow" style="left:193px;top:374px"><div class="tile-face"><div class="badge"><span>MISS</span><span>a turn</span></div></div></div>
  <div class="tile tile--side tile--orange" style="left:193px;top:446px"><div class="tile-face">45<sup>%</sup></div></div>
  <div class="tile tile--side tile--orange" style="left:193px;top:518px"><div class="tile-face">45<sup>%</sup></div></div>

  <!-- right column -->
  <div class="tile tile--side tile--right tile--green" style="left:937px;top:230px"><div class="tile-face">35<sup>%</sup></div></div>
  <div class="tile tile--side tile--right tile--green" style="left:937px;top:302px"><div class="tile-face">35<sup>%</sup></div></div>
  <div class="tile tile--side tile--right tile--yellow" style="left:937px;top:374px"><div class="tile-face"><div class="badge"><span>MISS</span><span>a turn</span></div></div></div>
  <div class="tile tile--side tile--right tile--orange" style="left:937px;top:446px"><div class="tile-face">45<sup>%</sup></div></div>
  <div class="tile tile--side tile--right tile--orange" style="left:937px;top:518px"><div class="tile-face">45<sup>%</sup></div></div>

  <h1 class="title"><span class="title-word">try</span><span class="title-ratio">45:35:20</span></h1>

  <p class="credit credit--bottom">© Dana Wells, Collegium of Skill Advisors  www.csaglobalnet.org</p>
  <p class="credit credit--top">© Dana Wells, Collegium of Skill Advisors  www.csaglobalnet.org</p>
</div>
</body>
</html>
```